Fallow Business Card Design

Photography business needs a logo. I would like to see creative licence on options on 1 & 2 sided. I really like the concept of a fully / partially frosted design. I have already used Brandloom for my Logo, so I am looking for the same level of assistance with this project.

Industry/Entity Type

Business

Font styles to use
Serif
Script

Requirements
Must have
• Must Have:
• - These are my contact details
• Name: Pat L Fallow
• Mobile: 5183920471
• email: marlaquist@postvane.com

```html
<!DOCTYPE html>
<html lang="en">
<head>
<meta charset="utf-8">
<title>Fallow Business Card</title>
<link rel="stylesheet" href="https://fonts.googleapis.com/css2?family=Open+Sans:wght@400;700&display=swap">
<style>
  :root {
    --backdrop: #1d1d1f;
    --card-front: #ffffff;
    --card-back: #74c8e9;
    --mark-soft: #8ea2dc;
    --ink-dark: #2a2a2c;
    --ink-light: #ffffff;
  }
  html, body {
    margin: 0;
    padding: 0;
    width: 1200px;
    height: 800px;
    overflow: hidden;
    background: var(--backdrop);
    font-family: "Open Sans", Arial, sans-serif;
  }
  .stage {
    position: relative;
    width: 1200px;
    height: 800px;
  }
  .card {
    position: absolute;
    width: 525px;
    height: 300px;
    box-shadow: 0 12px 30px rgba(0, 0, 0, 0.45);
  }
  .card--front {
    left: 50px;
    top: 250px;
    background: var(--card-front);
    display: flex;
    align-items: center;
    justify-content: center;
  }
  .card--back {
    left: 625px;
    top: 250px;
    background: var(--card-back);
  }
  .brand {
    display: flex;
    align-items: center;
    gap: 14px;
    font-weight: 700;
  }
  .brand__dot {
    border-radius: 50%;
  }
  .brand--front {
    color: var(--mark-soft);
    font-size: 54px;
  }
  .brand--front .brand__dot {
    width: 44px;
    height: 44px;
    background: var(--mark-soft);
  }
  .brand--back {
    position: absolute;
    left: 48px;
    top: 186px;
    color: var(--ink-dark);
    font-size: 34px;
  }
  .brand--back .brand__dot {
    width: 30px;
    height: 30px;
    background: var(--ink-dark);
  }
  .contact {
    position: absolute;
    left: 270px;
    top: 62px;
  }
  .contact__name {
    margin: 0;
    color: var(--ink-dark);
    font-size: 17px;
    font-weight: 700;
    line-height: 1.2;
  }
  .contact__role {
    margin: 0 0 22px;
    color: var(--ink-light);
    font-size: 11px;
  }
  .contact__row {
    display: flex;
    align-items: center;
    gap: 12px;
    margin: 0 0 14px;
    color: var(--ink-light);
    font-size: 11.5px;
  }
  .contact__icon {
    width: 14px;
    height: 14px;
    flex: none;
  }
</style>
</head>
<body>
<main class="stage">
  <section class="card card--front" aria-label="Card front">
    <div class="brand brand--front">
      <span class="brand__dot"></span>
      <span class="brand__name">Fallow</span>
    </div>
  </section>

  <section class="card card--back" aria-label="Card back">
    <div class="brand brand--back">
      <span class="brand__dot"></span>
      <span class="brand__name">Fallow</span>
    </div>

    <div class="contact">
      <h1 class="contact__name">Pat L Fallow</h1>
      <p class="contact__role">Photo Manager</p>
      <p class="contact__row">
        <svg class="contact__icon" viewBox="0 0 14 14" aria-hidden="true">
          <rect x="3.5" y="0.8" width="7" height="12.4" rx="1.2" fill="none" stroke="#2a2a2c" stroke-width="1.3"/>
          <line x1="6" y1="11" x2="8" y2="11" stroke="#2a2a2c" stroke-width="1.2"/>
        </svg>
        <span>Mobile: 5183920471</span>
      </p>
      <p class="contact__row">
        <svg class="contact__icon" viewBox="0 0 14 14" aria-hidden="true">
          <rect x="1" y="3" width="12" height="8.5" fill="#2a2a2c"/>
          <polyline points="1,3 7,8 13,3" fill="none" stroke="#74c8e9" stroke-width="1"/>
        </svg>
        <span>Email: marlaquist@postvane.com</span>
      </p>
    </div>
  </section>
</main>
</body>
</html>
```